KORVEL Flyer

We need a flyer for the research project called 'KORVEL'. We will distribute this flyer during conferences and events to our audience (mainly industry (Security and IoT), medical organisations, and researchers) in order to provide the basic information about the project.
The project will provide a Holistic Network Guard Framework for the Health-Care Industry.
We are attaching files to provide with concrete information on our requirements:
- KORVEL brochure content_final.ppt: includes the content we would like to include in the flyer. There is also the URL to the project website
- KORVEL layout.doc: it includes information about the layout (example video from another project brochure)
- KORVEL logo final version_sourcefile.zip: the project logo
- Logo-partners.zip: Logos that will be included (please follow the numbered order.)
We would like to use colors that belong to the project logo color range. Regarding the images that you may include in the brochure we wouldn't like to propose any because we do not want to limitate your imagination. They could be relevant to medical devices, security, etc.

```html
<!DOCTYPE html>
<html lang="en">
<head>
<meta charset="utf-8">
<title>KORVEL Flyer</title>
<link rel="stylesheet" href="https://fonts.googleapis.com/css2?family=Exo+2:wght@400;500;600;800&display=swap">
<style>
  :root {
    --green: #1b9c80;
    --green-dark: #0e6f5b;
    --green-deep: #0a5646;
    --teal-text: #17a08a;
    --paper: #f7f7f7;
    --white: #ffffff;
    --stage: #e4e4e4;
  }
  * { box-sizing: border-box; margin: 0; padding: 0; }
  html, body { width: 1200px; height: 824px; overflow: hidden; }
  body {
    background: var(--stage);
    font-family: "Exo 2", sans-serif;
    display: flex;
  }
  .page {
    position: relative;
    width: 600px;
    height: 824px;
    background: var(--paper);
    overflow: hidden;
  }
  .page + .page { border-left: 1px solid #d6d6d6; }
  .page__art { position: absolute; inset: 0; width: 600px; height: 824px; }

  .brand {
    position: absolute;
    display: flex;
    align-items: center;
    gap: 10px;
    color: var(--teal-text);
    font-weight: 500;
    font-size: 34px;
    letter-spacing: 2px;
  }
  .brand__dot {
    width: 30px; height: 30px;
    border-radius: 50%;
    border: 3px solid var(--teal-text);
  }
  .back-cover .brand { right: 60px; bottom: 70px; }

  .topics {
    position: absolute;
    top: 38px; left: 54px;
    list-style: none;
    color: var(--white);
    font-size: 12px;
    line-height: 1.45;
  }
  .topics li::before { content: "• "; }
  .topics .indent { padding-left: 10px; }

  .cover-title {
    position: absolute;
    top: 250px; right: 50px;
    width: 420px;
    text-align: right;
    color: var(--white);
    font-weight: 800;
    font-size: 30px;
    line-height: 1.12;
    text-transform: uppercase;
  }

  .join {
    position: absolute;
    left: 40px; top: 620px;
    color: var(--teal-text);
  }
  .join__heading { font-weight: 800; font-size: 16px; margin-bottom: 8px; }
  .join__list { list-style: none; font-size: 15px; line-height: 1.3; }
  .join__list li { display: flex; align-items: center; gap: 8px; }
  .join__icon {
    width: 11px; height: 11px;
    background: var(--teal-text);
    border-radius: 2px;
    flex: none;
  }
  .front-cover .brand { right: 50px; top: 640px; font-size: 30px; }
</style>
</head>
<body>

  <section class="page back-cover">
    <svg class="page__art" viewBox="0 0 600 824" role="img" aria-label="Green-tinted photograph of an ultrasound monitor in a hospital operating room">
      <defs>
        <linearGradient id="backPhoto" x1="0" y1="0" x2="1" y2="1">
          <stop offset="0" stop-color="#1f9f83"/>
          <stop offset="0.55" stop-color="#137f69"/>
          <stop offset="1" stop-color="#0a5a49"/>
        </linearGradient>
      </defs>
      <path d="M0 0 H600 V600 C470 690 270 740 0 745 Z" fill="url(#backPhoto)"/>
    </svg>
    <div class="brand"><span class="brand__dot"></span>KORVEL</div>
  </section>

  <section class="page front-cover">
    <svg class="page__art" viewBox="0 0 600 824" role="img" aria-label="Green-tinted close-up photograph of a stethoscope on a desk">
      <defs>
        <linearGradient id="frontPhoto" x1="0" y1="0" x2="1" y2="1">
          <stop offset="0" stop-color="#22a387"/>
          <stop offset="0.6" stop-color="#168a71"/>
          <stop offset="1" stop-color="#0f6f5b"/>
        </linearGradient>
      </defs>
      <path d="M0 0 H600 V520 C520 540 380 555 260 560 C210 562 190 590 130 590 C80 590 40 575 0 572 Z" fill="url(#frontPhoto)"/>
    </svg>

    <ul class="topics">
      <li>Healthcare Services</li>
      <li>Medical and Health Devices</li>
      <li>Cybersecurity Vulnerability</li>
      <li class="indent">Assessment and Certification</li>
      <li>Cybersecurity</li>
      <li>Data privacy</li>
    </ul>

    <h1 class="cover-title">A Holistic Network Guard Framework for the Health-Care Industry</h1>

    <div class="join">
      <p class="join__heading">JOIN US:</p>
      <ul class="join__list">
        <li><span class="join__icon"></span>@ProjectKorvel</li>
        <li><span class="join__icon"></span>korvel-project.eu</li>
        <li><span class="join__icon"></span>korvel-project</li>
        <li><span class="join__icon"></span>The korvel project eu</li>
        <li><span class="join__icon"></span>https://korvel-project.eu/</li>
      </ul>
    </div>

    <div class="brand"><span class="brand__dot"></span>KORVEL</div>
  </section>

</body>
</html>
```